public page walrus GX (www.walrusgx.com)

https://www.quillbarn.net/shard/s412/sh/a3b1c9d2-58e4-4f7a-b2c6-1d9e0f7a3b45/41c7e2a9d08b6f53e17a92c4d6b0f831

compatible with wordpress

Designs look the same

Industry/Entity Type

Finance And Accounting

Coding

Coded - Design and coding required

Number of Pages Required

1 page

Font styles to use
Sans Serif

Colors
85cae6
3176b5
cfdeed
fac994
fff3d1
fefdec
cfcfcf
e8e8e8
9d9d9d

```html
<!DOCTYPE html>
<html lang="en">
<head>
<meta charset="utf-8">
<title>walrus GX — Calculate your numbers</title>
<link href="https://fonts.googleapis.com/css2?family=Montserrat:wght@300;400;500;600;700&display=swap" rel="stylesheet">
<style>
:root{
  --violet:#6b4cf2;
  --blue:#3176b5;
  --teal:#2fb0c6;
  --sky:#85cae6;
  --ice:#cfdeed;
  --orange:#fbb22c;
  --peach:#fac994;
  --cream:#fff3d1;
  --ink:#1e1e2a;
  --text:#4a4a55;
  --muted:#9d9d9d;
  --line:#e8e8e8;
  --grey:#cfcfcf;
  --white:#ffffff;
}
*{box-sizing:border-box;margin:0;padding:0}
html,body{width:1200px;height:3863px;overflow:hidden;background:var(--white)}
body{font-family:'Montserrat',Arial,sans-serif;color:var(--text);position:relative}
.page{position:relative;width:1200px;height:3863px;overflow:hidden}
.abs{position:absolute}
.btn{position:absolute;background:var(--orange);color:var(--white);font-weight:600;font-size:14px;border-radius:22px;display:flex;align-items:center;justify-content:center;box-shadow:0 6px 14px rgba(251,178,44,.35)}
/* hero */
.hero{position:absolute;left:0;top:0;width:1200px;height:560px;background:linear-gradient(110deg,var(--violet) 0%,#4f6cf0 45%,var(--teal) 100%)}
.hero-curve{position:absolute;left:0;top:440px}
.deco{position:absolute;background:rgba(255,255,255,.12);border-radius:14px}
.brand{position:absolute;left:147px;top:24px;display:flex;align-items:center;gap:10px;color:var(--white);font-weight:600;font-size:17px}
.brand .mark{width:30px;height:30px;border-radius:50%;background:var(--white)}
.nav-link{position:absolute;top:33px;color:var(--white);font-size:13px;font-weight:500;white-space:nowrap}
.login{position:absolute;left:904px;top:26px;width:72px;height:28px;border:1.5px solid var(--white);border-radius:4px;color:var(--white);font-size:12px;display:flex;align-items:center;justify-content:center}
.signup{position:absolute;left:982px;top:26px;width:72px;height:28px;background:var(--orange);border-radius:4px;color:var(--white);font-size:12px;display:flex;align-items:center;justify-content:center}
.hero-title{position:absolute;left:0;width:1200px;top:110px;text-align:center;color:var(--white);font-size:50px;font-weight:300;letter-spacing:1px}
.hero-sub{position:absolute;left:0;width:1200px;top:172px;text-align:center;color:var(--white);font-size:18px;font-weight:500;letter-spacing:5px}
.signup-form{position:absolute;left:386px;top:226px;width:430px;height:46px;background:var(--white);border-radius:23px;box-shadow:0 8px 20px rgba(0,0,0,.15)}
.signup-form span{position:absolute;left:24px;top:14px;font-size:14px;color:var(--muted)}
.signup-form .btn{left:312px;top:0;width:118px;height:46px;box-shadow:none}
.sq{position:absolute;border-radius:12px}
/* features */
h2.feature-title{position:absolute;font-size:31px;font-weight:400;color:var(--ink);line-height:1.22}
.feature-copy{position:absolute;font-size:14px;line-height:1.75;color:var(--text)}
.partner-row{position:absolute;display:flex;gap:34px;align-items:center;font-size:20px;font-weight:600;color:var(--grey)}
.partner-row i{display:inline-block;width:18px;height:18px;border-radius:50%;background:var(--grey);margin-right:7px;vertical-align:-2px}
.quote{position:absolute;font-style:italic;color:var(--muted);font-size:15px;line-height:1.75}
.author{position:absolute;display:flex;align-items:center;gap:16px}
.author .avatar{width:50px;height:50px;border-radius:50%;background:var(--line)}
.author b{display:block;font-size:11px;color:var(--ink);font-weight:700}
.author small{font-size:11px;color:var(--muted)}
/* plan */
.plan{position:absolute;left:0;top:2189px;width:1200px;height:386px;background:linear-gradient(180deg,#ffffff 0%,#f3f3f5 100%);border-top:1px solid var(--line)}
.plan-mark{position:absolute;left:562px;top:72px;width:76px;height:76px;border-radius:50%;border:5px solid var(--ink)}
.plan-title{position:absolute;left:0;width:1200px;top:158px;text-align:center;font-size:28px;color:var(--ink);font-weight:400}
.plan-price{position:absolute;left:0;width:1200px;top:196px;text-align:center;font-size:52px;color:var(--ink);font-weight:400}
/* faq */
.faq-title{position:absolute;left:0;width:1200px;top:2632px;text-align:center;font-size:31px;color:var(--ink);font-weight:400}
.faq-tabs{position:absolute;left:384px;top:2700px;width:432px;display:flex;justify-content:space-between;font-size:13px;font-weight:600;color:var(--muted);border-bottom:1px solid var(--line);padding-bottom:10px}
.faq-tabs .active{color:var(--ink);position:relative}
.faq-tabs .active::after{content:"";position:absolute;left:0;right:0;bottom:-11px;height:2px;background:var(--ink)}
.faq-item{position:absolute;left:198px;width:788px;height:70px;border-bottom:1px solid var(--line);display:flex;align-items:center;justify-content:space-between;font-size:17px;color:var(--text)}
.faq-item.open{color:var(--ink);font-weight:500;border-bottom:none;height:58px}
.toggle{width:22px;height:22px;border-radius:50%;background:var(--line);display:flex;align-items:center;justify-content:center;font-size:16px;color:var(--ink);font-weight:600}
.faq-answer{position:absolute;left:198px;top:2882px;width:788px;height:118px;background:#f1f6fb;padding:20px 30px;font-size:12.5px;line-height:1.85;color:var(--text)}
/* partners */
.partners{position:absolute;left:0;top:3296px;width:1200px;height:304px;background:linear-gradient(110deg,var(--violet) 0%,#4f6cf0 45%,var(--teal) 100%);overflow:hidden}
.partners h2{position:absolute;left:0;width:1200px;top:50px;text-align:center;color:var(--white);font-size:32px;font-weight:400}
.partner-box{position:absolute;top:124px;width:184px;height:78px;background:var(--white);display:flex;align-items:center;justify-content:center;font-size:22px;font-weight:600;color:var(--grey)}
.dots{position:absolute;left:560px;top:242px;display:flex;gap:10px}
.dots span{width:6px;height:6px;border-radius:50%;background:rgba(255,255,255,.6)}
.dots span:first-child{background:var(--white)}
/* footer */
.footer{position:absolute;left:0;top:3600px;width:1200px;height:263px;background:var(--white)}
.foot-mark{position:absolute;left:188px;top:52px;width:56px;height:56px;border-radius:50%;border:4px solid var(--ink)}
.contact{position:absolute;left:188px;top:124px;font-size:12px;line-height:2.05;color:var(--text)}
.contact svg{vertical-align:-2px;margin-right:8px}
.foot-col{position:absolute;top:50px;font-size:12px;line-height:2;color:var(--text)}
.foot-col h4{font-size:14px;font-weight:600;color:var(--ink);margin-bottom:6px}
.copyright{position:absolute;left:188px;top:228px;font-size:11px;color:var(--muted)}
.social{position:absolute;left:938px;top:224px;display:flex;gap:8px}
.social span{width:18px;height:18px;border:1.5px solid var(--muted);border-radius:50%}
</style>
</head>
<body>
<div class="page">

<section class="hero">
  <div class="deco" style="left:110px;top:140px;width:90px;height:90px;transform:rotate(12deg)"></div>
  <div class="deco" style="left:20px;top:280px;width:70px;height:70px;transform:rotate(-8deg)"></div>
  <div class="deco" style="left:980px;top:60px;width:100px;height:100px;transform:rotate(10deg)"></div>
  <div class="deco" style="left:1040px;top:270px;width:120px;height:120px;transform:rotate(-12deg)"></div>
  <div class="deco" style="left:860px;top:140px;width:50px;height:50px;transform:rotate(20deg)"></div>

  <div class="brand"><span class="mark"></span>walrus GX</div>
  <nav>
    <span class="nav-link" style="left:435px">Pricing</span>
    <span class="nav-link" style="left:508px">About us</span>
    <span class="nav-link" style="left:594px">Contacts</span>
    <span class="nav-link" style="left:677px">Blog</span>
    <span class="nav-link" style="left:742px">FAQ's</span>
  </nav>
  <div class="login">Login</div>
  <div class="signup">Sign-up</div>

  <h1 class="hero-title">CALCULATE YOUR NUMBERS</h1>
  <p class="hero-sub">Easier like never before</p>
  <div class="signup-form"><span>Your Email Address</span><div class="btn">Get Started</div></div>
</section>
<svg class="hero-curve" width="1200" height="130" viewBox="0 0 1200 130" aria-hidden="true">
  <path d="M0 70 C300 20 600 40 820 50 C1000 58 1100 30 1200 10 L1200 130 L0 130 Z" fill="#ffffff"/>
</svg>

<div class="abs" role="img" aria-label="Laptop showing the finance dashboard with statistics cards, area chart, bar list and donut chart" style="left:272px;top:314px;width:656px;height:380px;border-radius:14px 14px 4px 4px;background:linear-gradient(180deg,#e9eef5 0%,#cfdeed 100%);box-shadow:0 20px 40px rgba(0,0,0,.12)"></div>
<div class="sq" style="left:340px;top:316px;width:62px;height:62px;background:linear-gradient(135deg,#4a7cf0,#6b4cf2);transform:rotate(12deg)"></div>
<div class="sq" style="left:198px;top:528px;width:58px;height:58px;background:var(--orange);transform:rotate(-10deg)"></div>
<div class="sq" style="left:913px;top:512px;width:54px;height:54px;background:linear-gradient(135deg,#6b4cf2,#3176b5);transform:rotate(14deg)"></div>
<div class="sq" style="left:475px;top:640px;width:54px;height:54px;background:linear-gradient(135deg,#4a7cf0,#6b4cf2);transform:rotate(-14deg)"></div>

<div class="abs" role="img" aria-label="Wireframe illustration of a desktop window and a phone screen" style="left:180px;top:790px;width:390px;height:320px;border-radius:10px;background:linear-gradient(160deg,#f6f9fd 0%,#e4edf8 100%)"></div>
<h2 class="feature-title" style="left:643px;top:836px">Our good feedbacks and<br>statistics shows all</h2>
<div class="partner-row" style="left:643px;top:928px"><span><i></i>Cartwell</span><span><i></i>Shopnest</span><span><i></i>Chatterly</span></div>
<p class="feature-copy" style="left:643px;top:978px;width:400px">A big part of our design process is validation and nailing the details. Pixelway lets us iterate quickly, elevate quality, and ship fast.</p>
<div class="btn" style="left:635px;top:1087px;width:122px;height:40px">Get Started</div>
<div class="sq" style="left:1082px;top:836px;width:14px;height:14px;border-radius:50%;background:var(--orange)"></div>

<svg class="abs" style="left:580px;top:1230px" width="620" height="520" viewBox="0 0 620 520" aria-hidden="true">
  <path d="M120 60 C260 -10 520 20 620 0 L620 520 C480 500 300 520 180 470 C40 410 0 300 40 200 C60 140 80 90 120 60 Z" fill="#f4f8fc"/>
</svg>
<svg class="abs" style="left:0;top:1640px" width="420" height="160" viewBox="0 0 420 160" aria-hidden="true">
  <path d="M0 20 C140 0 300 40 420 120 L420 160 L0 160 Z" fill="#f4f8fc"/>
</svg>
<div class="sq" style="left:320px;top:1238px;width:20px;height:20px;border-radius:4px;background:#4a7cf0"></div>
<div class="sq" style="left:806px;top:1206px;width:16px;height:16px;border-radius:4px;background:#4a7cf0"></div>
<div class="sq" style="left:525px;top:1656px;width:26px;height:26px;border-radius:5px;background:var(--orange)"></div>
<div class="sq" style="left:96px;top:1680px;width:14px;height:14px;border-radius:4px;background:#4a7cf0"></div>
<div class="sq" style="left:1028px;top:1742px;width:22px;height:22px;border-radius:4px;background:#4a7cf0"></div>
<h2 class="feature-title" style="left:175px;top:1310px">Don't miss your chance<br>to grow business</h2>
<div class="abs" style="left:175px;top:1404px;font-size:26px;font-weight:600;color:var(--ink)">orinoco</div>
<p class="feature-copy" style="left:175px;top:1462px;width:380px">A big part of our design process is validation and nailing the details. Pixelway lets us iterate quickly, elevate quality, and ship fast.</p>
<div class="btn" style="left:170px;top:1574px;width:122px;height:40px">Get Started</div>
<div class="abs" role="img" aria-label="Laptop and tablet showing dashboard charts and a world map" style="left:605px;top:1338px;width:530px;height:234px;border-radius:10px;background:linear-gradient(180deg,#eef3f9 0%,#d6e3f0 100%);box-shadow:0 14px 30px rgba(0,0,0,.1)"></div>

<div class="abs" role="img" aria-label="Hand holding a smartphone showing a task list app" style="left:129px;top:1800px;width:386px;height:380px;border-radius:18px;background:linear-gradient(160deg,#f2f5f9 0%,#e8d9cc 100%)"></div>
<h2 class="feature-title" style="left:623px;top:1816px">Our good feedbacks and<br>statistics shows all</h2>
<p class="quote" style="left:623px;top:1904px;width:400px">"A big part of our design process is validation and nailing the details. Pixelway lets us iterate quickly, elevate quality, and ship fast."</p>
<svg class="abs" style="left:945px;top:1970px" width="54" height="40" viewBox="0 0 54 40" aria-hidden="true">
  <path d="M4 40 V22 C4 10 10 4 22 2 V10 C14 12 12 16 12 22 H22 V40 Z M32 40 V22 C32 10 38 4 50 2 V10 C42 12 40 16 40 22 H50 V40 Z" fill="#e2e2e2"/>
</svg>
<div class="author" style="left:619px;top:2008px"><span class="avatar"></span><div><b>DANA HOLT</b><small>Founder, CEO</small></div></div>
<div class="btn" style="left:619px;top:2086px;width:122px;height:40px">Get Started</div>

<section class="plan">
  <div class="plan-mark"></div>
  <h2 class="plan-title">Grab Our Plan This Weekend</h2>
  <p class="plan-price">$19,99 / month</p>
  <div class="btn" style="left:505px;top:272px;width:180px;height:44px">Check Plans</div>
</section>

<h2 class="faq-title">FREQUENTLY ASKED QUESTIONS</h2>
<div class="faq-tabs"><span class="active">PRICING</span><span>DISCOUNTS</span><span>HOW IT WORKS</span><span>MOBILE</span></div>
<div class="faq-item" style="top:2754px">Answer for a way way longer question with longer answer<span class="toggle">+</span></div>
<div class="faq-item open" style="top:2824px">Answer for some kind of question<span class="toggle">–</span></div>
<div class="faq-answer">Lorem ipsum dolor sit amet, consectetuer adipiscing elit. Aenean commodo ligula eget dolor. Aenean massa. Cum sociis natoque penatibus et magnis dis parturient montes, nascetur ridiculus mus. Donec quam felis, ultricies nec, pellentesque eu, pretium quis, sem. Nulla consequat massa quis enim. Donec pede justo, fringilla vel, aliquet nec.</div>
<div class="faq-item" style="top:3006px">How much cost your plan to buy for a year?<span class="toggle">+</span></div>
<div class="faq-item" style="top:3076px">Do you have something like free trial for this program?<span class="toggle">+</span></div>
<div class="faq-item" style="top:3146px">Where I can find you in a local place?<span class="toggle">+</span></div>

<section class="partners">
  <div class="deco" style="left:40px;top:30px;width:90px;height:90px;transform:rotate(14deg)"></div>
  <div class="deco" style="left:1000px;top:160px;width:110px;height:110px;transform:rotate(-10deg)"></div>
  <div class="deco" style="left:1080px;top:20px;width:60px;height:60px;transform:rotate(8deg)"></div>
  <h2>Our Partners</h2>
  <div class="partner-box" style="left:198px">Launchfund</div>
  <div class="partner-box" style="left:403px">Cartwell</div>
  <div class="partner-box" style="left:600px">Shopnest</div>
  <div class="partner-box" style="left:801px">Chatterly</div>
  <div class="dots"><span></span><span></span><span></span><span></span></div>
</section>

<footer class="footer">
  <div class="foot-mark"></div>
  <div class="contact">
    <div><svg width="12" height="12" viewBox="0 0 12 12"><path d="M2 1 L4 1 L5 4 L3.5 5 C4 6.5 5.5 8 7 8.5 L8 7 L11 8 L11 10 C11 11 10 11 9 11 C4.5 10.5 1.5 7.5 1 3 C1 2 1 1 2 1 Z" fill="#4a4a55"/></svg>+370 612 345 67</div>
    <div><svg width="12" height="10" viewBox="0 0 12 10"><rect x="0.5" y="0.5" width="11" height="9" fill="none" stroke="#4a4a55"/><path d="M0.5 0.5 L6 5.5 L11.5 0.5" fill="none" stroke="#4a4a55"/></svg>info@walrusgx.com</div>
    <div style="padding-left:20px">Company Name</div>
  </div>
  <div class="foot-col" style="left:417px"><h4>About walrus GX</h4>Newsletter<br>Our Memberships<br>Events<br>Investors<br>Supplier Guide</div>
  <div class="foot-col" style="left:649px"><h4>Account</h4>Manage Your ID<br>walrus GX Store<br>Customer Reviews<br>Ask a Question<br>Why choose us?</div>
  <div class="foot-col" style="left:868px"><h4>Apie Mus</h4>Inclusion and Diversity<br>Supplier Responsibility<br>Inclusion and Diversity<br>Shop for Business<br>Shop for Education</div>
  <div class="copyright">Copyright 2018 walrus GX | All rights reserved</div>
  <div class="social"><span></span><span></span><span></span></div>
</footer>

</div>
</body>
</html>
```